Brisk Meadow LLC business card

I created a front and back idea of what I want. Also I included my Brisk Meadow logo to be used on the card. Please use your creativity to make it look professional and awesome! Use the all text and phrases in the sample card that I made.

(Front of card)Key words and phrases:
FOOD GROWING MACHINES
Aeroponics Technology
No soil
No pesticides
98% less water
Grow year round

(Back of card)
EVERY MONTH ONE PILLAR PLOT WILL BE GIVEN AWAY
FOLLOW US ON IG FOR A CHANCE TO WIN A PILLAR PLOT
FOOD GROWING MACHINES
Vertical Farming
Urban Farming
100% Organic
Grows 40% Faster
Indoors/outdoors

My contact info:
Chef Rux
Phone:415 730-2918
web: briskmeadow.example
IG: briskmeadowco

Target Market(s)

urban farming, vertical farming gardening

Industry/Entity Type

Gardening

Contact Information for Business Card

Front of card)Key words and phrases:
FOOD GROWING MACHINES
Aeroponics Technology
No soil
No pesticides
98% less water
Grow year round

(Back of card)
FOOD GROWING MACHINES
Vertical Farming
Urban Farming
100% Organic
Grows 40% Faster
Indoors/outdoors

My contact info:
Phone:415 730-2918
web: briskmeadow.example
IG: briskmeadowco

Requirements
Must have
• My contact info:
Chef Rux
Phone:415 730-2918
web: briskmeadow.example
IG: briskmeadowco
Nice to have
• Great imagery and easy to read. Try to incorporate the image that I uploaded of the little girl.

```html
<!DOCTYPE html>
<html lang="en">
<head>
<meta charset="utf-8">
<title>Brisk Meadow – Business Card</title>
<link href="https://fonts.googleapis.com/css2?family=Bebas+Neue&family=Roboto+Condensed:wght@400;500&display=swap" rel="stylesheet">
<style>
  :root {
    --backdrop: #282828;
    --paper: #ffffff;
    --lime: #8cff00;
    --lime-text: #86f000;
    --leaf-dark: #66c400;
    --forest: #2b5200;
    --ink-dark: #1c3300;
    --white: #ffffff;
    --photo-top: #4a4a44;
    --photo-mid: #7a6a66;
    --photo-leaf: #5f9a3a;
  }
  * { margin: 0; padding: 0; box-sizing: border-box; }
  html, body { width: 1200px; height: 801px; overflow: hidden; }
  body {
    background: var(--backdrop);
    position: relative;
    font-family: "Roboto Condensed", "Arial Narrow", sans-serif;
  }
  .card {
    position: absolute;
    top: 274px;
    width: 443px;
    height: 263px;
    overflow: hidden;
    background: var(--paper);
  }
  .card--back { left: 153px; }
  .card--front { left: 625px; }
  .card__wave { position: absolute; inset: 0; width: 100%; height: 100%; }
  .card__photo {
    position: absolute; inset: 0;
    background:
      linear-gradient(90deg, var(--photo-top) 0%, var(--photo-mid) 38%, #c9cbc4 57%, var(--photo-leaf) 70%, #8fc060 100%);
  }
  .heading {
    position: absolute;
    font-family: "Bebas Neue", "Oswald", sans-serif;
    line-height: 1;
    white-space: nowrap;
  }
  .promo { color: var(--lime-text); left: 23px; }
  .promo--monthly { top: 21px; font-size: 22px; letter-spacing: 0.3px; }
  .promo--follow { top: 50px; font-size: 20px; letter-spacing: -0.1px; }
  .brand-name {
    color: var(--lime-text);
    left: 304px; top: 83px;
    font-size: 25px; line-height: 21px;
    letter-spacing: 0.5px;
  }
  .owner-name { color: var(--lime-text); left: 318px; top: 150px; font-size: 22px; }
  .tagline { color: var(--forest); font-size: 21px; letter-spacing: 0.4px; }
  .card--back .tagline { left: 24px; top: 168px; }
  .card--front .tagline { left: 18px; top: 176px; }
  .features { position: absolute; color: var(--white); font-size: 15px; line-height: 1; white-space: nowrap; }
  .features span { position: absolute; }
  .card--back .features { left: 24px; top: 199px; }
  .contact {
    position: absolute; right: 24px; top: 204px;
    color: var(--white); font-size: 13px; line-height: 15.5px;
    text-align: right;
  }
  .contact li { list-style: none; display: flex; justify-content: flex-end; align-items: center; gap: 4px; }
  .contact svg { width: 11px; height: 11px; flex: none; }
  .tech { position: absolute; left: 22px; top: 198px; color: var(--white); font-size: 17px; line-height: 1; }
  .benefits { position: absolute; left: 0; top: 233px; color: var(--ink-dark); font-size: 14.5px; line-height: 1; white-space: nowrap; }
  .benefits span { position: absolute; }
</style>
</head>
<body>

<section class="card card--back">
  <svg class="card__wave" viewBox="0 0 443 263" preserveAspectRatio="none" aria-hidden="true">
    <path fill="var(--leaf-dark)" d="M0,124 C30,98 60,88 87,88 C150,88 230,140 280,165 C320,185 345,188 360,188 C400,188 425,165 443,140 L443,263 L0,263Z"/>
    <path fill="var(--lime)" d="M0,136 C30,110 62,100 92,100 C155,100 230,145 282,168 C322,186 345,188 360,188 C400,188 425,165 443,140 L443,263 L0,263Z"/>
  </svg>
  <p class="heading promo promo--monthly">Every month one Pillar Plot will be given away</p>
  <p class="heading promo promo--follow">Follow us on IG for a chance to win a Pillar Plot</p>
  <p class="heading brand-name">Brisk<br>Meadow</p>
  <p class="heading owner-name">Chef Rux</p>
  <p class="heading tagline">Food Growing Machines</p>
  <div class="features">
    <span style="left:0;top:0">Vertical Farming</span>
    <span style="left:114px;top:0">Urban Farming</span>
    <span style="left:0;top:18px">100% Organic</span>
    <span style="left:95px;top:18px">Grows 40% Faster</span>
    <span style="left:0;top:36px">Indoors/outdoors</span>
  </div>
  <ul class="contact">
    <li>415 730-2918
      <svg viewBox="0 0 12 12" aria-hidden="true"><path fill="none" stroke="#fff" stroke-width="1.3" d="M3,1 L4.6,3.4 L3.6,4.6 C4.3,6.2 5.8,7.7 7.4,8.4 L8.6,7.4 L11,9 L10,11 C5.5,10.6 1.4,6.5 1,2Z"/></svg>
    </li>
    <li>www.briskmeadow.example
      <svg viewBox="0 0 12 12" aria-hidden="true"><g fill="none" stroke="#fff" stroke-width="1"><circle cx="6" cy="6" r="5"/><ellipse cx="6" cy="6" rx="2.2" ry="5"/><path d="M1,6H11M2,3.3H10M2,8.7H10"/></g></svg>
    </li>
    <li>briskmeadowco
      <svg viewBox="0 0 12 12" aria-hidden="true"><circle cx="6" cy="6" r="5" fill="none" stroke="#fff" stroke-width="1.2"/></svg>
    </li>
  </ul>
</section>

<section class="card card--front">
  <div class="card__photo" role="img" aria-label="Photo of a young girl tending a tall leafy vertical garden of chard indoors"></div>
  <svg class="card__wave" viewBox="0 0 443 263" preserveAspectRatio="none" aria-hidden="true">
    <path fill="var(--leaf-dark)" d="M0,152 C25,130 55,119 89,119 C150,119 215,175 250,200 C270,212 285,218 296,218 C350,218 410,200 443,173 L443,263 L0,263Z"/>
    <path fill="var(--lime)" d="M0,165 C28,142 58,131 92,131 C152,131 215,182 252,205 C272,215 285,218 296,218 C350,218 410,200 443,173 L443,263 L0,263Z"/>
  </svg>
  <p class="heading tagline">Food Growing Machines</p>
  <p class="tech">Aeroponics Technology</p>
  <div class="benefits">
    <span style="left:22px">No soil</span>
    <span style="left:75px">No pesticides</span>
    <span style="left:166px">98% less water</span>
    <span style="left:267px">Grow year round</span>
  </div>
</section>

</body>
</html>
```